Electrician Needs A Business Card

I already have a logo and would like a business card to be designed based around this logo the company is called Tolvane Electrical Pty Ltd

The business card will be printed on transparent plastic so I need it to stand out from the crowd. I do not want the card to have anything to do with Electrical on it eg light bulbs, power points etc

I need it to have the following details.

Gareth Pomfrey
Mobile : 0437 519 284
email : gareth@tolvaneelectrical.com.au

If it could incorporate the following onto the bottom of the card
ELECTRICAL - COMMUNICATIONS - AUDIO - VISUAL

```html
<!DOCTYPE html>
<html lang="en">
<head>
<meta charset="utf-8">
<title>Tolvane Electrical – Business Card</title>
<link href="https://fonts.googleapis.com/css2?family=Noto+Serif&family=Open+Sans:wght@400;700&display=swap" rel="stylesheet">
<style>
  :root {
    --page: #d8d3ca;
    --card-frost: #ebe9e4;
    --ink: #141414;
    --band: #0b0b0b;
    --amber: #f7a81b;
    --white: #ffffff;
  }
  * { box-sizing: border-box; margin: 0; padding: 0; }
  html, body { width: 1200px; height: 1023px; overflow: hidden; }
  body {
    background: var(--page);
    font-family: "Open Sans", Arial, sans-serif;
    position: relative;
  }
  .card {
    position: absolute;
    left: 150px; top: 236px;
    width: 900px; height: 550px;
    border-radius: 16px;
    overflow: hidden;
    background: var(--card-frost);
    box-shadow: 0 10px 30px rgba(0,0,0,.25);
  }
  .card-shapes { position: absolute; inset: 0; }
  .brand {
    position: absolute;
    left: 98px; top: 48px;
    display: flex; align-items: center; gap: 34px;
  }
  .brand-square {
    width: 250px; height: 250px;
    background: var(--amber);
    flex: none;
  }
  .brand-name {
    font-family: "Noto Serif", Georgia, serif;
    font-weight: 400;
    font-size: 76px;
    line-height: 1.0;
    color: var(--ink);
  }
  .contact {
    position: absolute;
    right: 55px; top: 352px;
    text-align: right;
    color: var(--white);
    font-size: 22px;
    line-height: 1.45;
  }
  .contact-name {
    color: var(--amber);
    font-weight: 700;
    font-size: 31px;
    line-height: 1.3;
  }
  .label { color: var(--amber); }
  .services {
    position: absolute;
    left: 0; right: 0; top: 488px; height: 62px;
    display: flex; align-items: center; justify-content: space-around;
    padding: 0 40px;
    color: var(--ink);
    font-size: 25px;
  }
  .service { display: flex; align-items: center; gap: 10px; }
  .service svg { width: 22px; height: 22px; fill: var(--ink); }
</style>
</head>
<body>
  <article class="card">
    <svg class="card-shapes" viewBox="0 0 900 550" aria-hidden="true">
      <polygon points="0,335 98,335 239,412 374,322 900,322 900,488 0,488" fill="var(--band)"/>
      <rect x="0" y="488" width="900" height="62" fill="var(--amber)"/>
    </svg>

    <div class="brand">
      <div class="brand-square"></div>
      <div class="brand-name">Tolvane<br>Electrical</div>
    </div>

    <div class="contact">
      <p class="contact-name">Gareth Pomfrey</p>
      <p><span class="label">Mobile :</span> 0437 519 284</p>
      <p><span class="label">email :</span> gareth@tolvaneelectrical.com.au</p>
    </div>

    <div class="services">
      <span class="service">
        <svg viewBox="0 0 24 24"><polygon points="14,1 5,14 11,14 9,23 19,9 13,9"/></svg>Electrical
      </span>
      <span class="service">
        <svg viewBox="0 0 24 24"><circle cx="12" cy="8" r="2.5"/><rect x="11" y="9" width="2" height="14"/><path d="M6 3a8 8 0 0 0 0 10l1.4-1.4a6 6 0 0 1 0-7.2zM18 3l-1.4 1.4a6 6 0 0 1 0 7.2L18 13a8 8 0 0 0 0-10z"/></svg>Communications
      </span>
      <span class="service">
        <svg viewBox="0 0 24 24"><polygon points="2,8 7,8 13,3 13,21 7,16 2,16"/><path d="M16 8a5 5 0 0 1 0 8l-1.2-1.2a3.5 3.5 0 0 0 0-5.6zM19 5a9 9 0 0 1 0 14l-1.2-1.2a7.3 7.3 0 0 0 0-11.6z"/></svg>Audio
      </span>
      <span class="service">
        <svg viewBox="0 0 24 24"><path d="M12 5C6 5 2 12 2 12s4 7 10 7 10-7 10-7-4-7-10-7zm0 11a4 4 0 1 1 0-8 4 4 0 0 1 0 8z"/><circle cx="12" cy="12" r="2"/></svg>Visual
      </span>
    </div>
  </article>
</body>
</html>
```